Harlow Brookworks highend custom homes

We build high end custom homes and timber frames we specialize in rustic hand made designs along with iron and concrete accents to add a modern touch 90% of my homes are buit on lake front properries attached is my logo and slogan as of now and my previous one

Target Market(s)

High end custom homes

Industry/Entity Type

Custom residential construction

Contact Information for Business Card

Been in buissness 8+ years inssured and reliable

Colors
A7469A
B969AE
D3A5CF
EDDBEB
F8F0F9

Requirements
Must have
• Must have slogan and phone number
Should not have
• A combination of rustic yet modern accents

```html
<!DOCTYPE html>
<html lang="en">
<head>
<meta charset="utf-8">
<title>Harlow Brookworks — Business Card</title>
<link href="https://fonts.googleapis.com/css2?family=Open+Sans:wght@400;700&display=swap" rel="stylesheet">
<style>
  :root {
    --forest: #4d5c49;
    --ink-grey: #666668;
    --mist: #dcdcde;
    --paper: #ffffff;
    --backdrop: #ffffff;
  }
  * { margin: 0; padding: 0; box-sizing: border-box; }
  html, body {
    width: 1200px;
    height: 1200px;
    overflow: hidden;
    background: var(--backdrop);
    font-family: "Open Sans", Arial, sans-serif;
  }
  .business-card {
    position: absolute;
    left: 162px;
    top: 342px;
    width: 867px;
    height: 558px;
    background: var(--paper);
    border: 2px solid var(--forest);
    border-radius: 47px;
    overflow: hidden;
  }
  .brand-mark {
    position: absolute;
    left: 67px;
    top: 63px;
    width: 167px;
    height: 167px;
    background: var(--forest);
  }
  .brand-name {
    position: absolute;
    left: 66px;
    top: 238px;
    font-weight: 700;
    font-size: 27px;
    line-height: 1;
    letter-spacing: 0.3px;
    color: var(--forest);
    text-transform: uppercase;
    white-space: nowrap;
  }
  .brand-slogan {
    position: absolute;
    left: 70px;
    top: 279px;
    font-weight: 400;
    font-size: 16px;
    line-height: 1;
    letter-spacing: 0.8px;
    color: var(--forest);
    text-transform: uppercase;
    white-space: nowrap;
  }
  .person {
    position: absolute;
    right: 41px;
    top: 72px;
    text-align: right;
  }
  .person-name {
    font-weight: 700;
    font-size: 39px;
    line-height: 1;
    letter-spacing: 0.8px;
    color: var(--forest);
    white-space: nowrap;
  }
  .person-title {
    margin-top: 10px;
    font-weight: 400;
    font-size: 28px;
    line-height: 1;
    color: var(--ink-grey);
  }
  .contact-list {
    position: absolute;
    left: 64px;
    top: 379px;
    list-style: none;
  }
  .contact-item {
    display: flex;
    align-items: center;
    height: 39px;
    font-size: 22px;
    color: var(--ink-grey);
    white-space: nowrap;
  }
  .contact-icon {
    width: 26px;
    height: 26px;
    margin-right: 20px;
    fill: var(--ink-grey);
    flex: none;
  }
  .decor-area {
    position: absolute;
    left: 547px;
    top: 231px;
    width: 320px;
    height: 327px;
    background: linear-gradient(135deg, rgba(220,220,222,0.15) 0%, var(--mist) 70%);
    border-top-left-radius: 160px;
  }
</style>
</head>
<body>
  <div class="business-card">
    <div class="decor-area" role="img" aria-label="Faint large decorative tool graphic in light grey"></div>

    <div class="brand-mark"></div>
    <div class="brand-name">Harlow Brookworks</div>
    <div class="brand-slogan">• From lodges to estates •</div>

    <div class="person">
      <div class="person-name">YOUR NAME HERE</div>
      <div class="person-title">Designation</div>
    </div>

    <ul class="contact-list">
      <li class="contact-item">
        <svg class="contact-icon" viewBox="0 0 24 24" aria-hidden="true">
          <path d="M6.6 10.8a15.1 15.1 0 0 0 6.6 6.6l2.2-2.2a1 1 0 0 1 1-.25 11.4 11.4 0 0 0 3.6.57 1 1 0 0 1 1 1V20a1 1 0 0 1-1 1A17 17 0 0 1 3 4a1 1 0 0 1 1-1h3.5a1 1 0 0 1 1 1c0 1.25.2 2.450.57 3.57a1 1 0 0 1-.25 1z"/>
        </svg>
        <span>+000-12345-6789</span>
      </li>
      <li class="contact-item">
        <svg class="contact-icon" viewBox="0 0 24 24" aria-hidden="true">
          <path d="M2 5h20v2l-10 6L2 7z M2 9l10 6 10-6v10H2z"/>
        </svg>
        <span>e-mail@mail.com</span>
      </li>
      <li class="contact-item">
        <svg class="contact-icon" viewBox="0 0 24 24" aria-hidden="true">
          <path d="M12 1a7.5 7.5 0 0 0-7.5 7.5C4.5 14 12 23 12 23s7.5-9 7.5-14.5A7.5 7.5 0 0 0 12 1zm0 10.3a2.8 2.8 0 1 1 0-5.6 2.8 2.8 0 0 1 0 5.6z"/>
        </svg>
        <span>Your Address here 0123456</span>
      </li>
    </ul>
  </div>
</body>
</html>
```